PebbleNest Preschool Flyer

Must include children who are of various races and colors and be within the age group of 2-5 years. No infant photos. Must have bright colors including red, yellow, green, and blue. Must include the logo.

We are a preschool that teaches Mandarin and Spanish too children ages 2-5. We are located in Washington, DC.

Target Market(s)

Parents from different ethnic backgrounds who would appreciate world language curriculum for their parents.

Industry/Entity Type

Childcare

Font styles to use
Serif

Colors
f04a51
0455a3
9bcb3c
fbed22

Requirements
Must have
• Must include children who are of various races and colors and be within the age group of 2-5 years. No infant photos. Must have bright colors including red, yellow, green, and blue. Must include the logo.
Nice to have
Should not have
• Just all Caucasian or all Asian children or children who look younger than 2 years old or older than 4 years old.

```html
<!DOCTYPE html>
<html lang="en">
<head>
<meta charset="utf-8">
<title>PebbleNest Preschool – Saturday Language Lessons</title>
<link rel="stylesheet" href="https://fonts.googleapis.com/css2?family=Crimson+Pro:wght@500&family=Arimo:wght@400;700&family=Noto+Sans+SC:wght@400&display=swap">
<style>
  :root {
    --red: #ec1c24;
    --brand-red: #f04a51;
    --yellow: #fbed22;
    --green: #9bcb3c;
    --green-deep: #2ea83a;
    --blue: #0455a3;
    --blue-bright: #0a74c4;
    --orange: #f57f20;
    --white: #ffffff;
  }
  * { margin: 0; padding: 0; box-sizing: border-box; }
  html, body { width: 927px; height: 1200px; overflow: hidden; background: var(--white); }
  .flyer { position: relative; width: 927px; height: 1200px; overflow: hidden; }
  .backdrop { position: absolute; inset: 0; }
  .brand {
    position: absolute; left: 0; right: 0; top: 205px; text-align: center;
    font-family: "Crimson Pro", "Times New Roman", serif; font-weight: 500;
    color: var(--red); font-size: 66px; line-height: 68px;
  }
  .brand-dot {
    position: absolute; left: 395px; top: 48px; width: 140px; height: 140px;
    border-radius: 50%; background: var(--red);
  }
  .banner { position: absolute; left: 0; top: 300px; overflow: visible; }
  .banner-text { font-family: "Arimo", Arial, sans-serif; font-weight: 700; fill: var(--white); font-size: 28px; }
  .kids-photo {
    position: absolute; left: 28px; top: 662px; width: 872px; height: 420px;
    background: linear-gradient(180deg, #f4f2ee 0%, #e9e4dc 55%, #d9cfc4 100%);
    border-radius: 6px;
  }
  .bubbles { position: absolute; left: 0; top: 560px; }
  .bubble-text { font-family: "Arimo", Arial, sans-serif; font-size: 22px; text-anchor: middle; }
  .bubble-han { font-family: "Noto Sans SC", sans-serif; font-size: 26px; text-anchor: middle; }
  .bubble-pinyin { font-family: "Arimo", Arial, sans-serif; font-size: 11px; text-anchor: middle; }
  .footer { position: absolute; left: 0; top: 1090px; width: 927px; height: 110px; color: var(--white); font-family: "Arimo", Arial, sans-serif; }
  .locations { position: absolute; left: 141px; top: 42px; font-size: 24px; letter-spacing: 0.5px; }
  .route-icon { position: absolute; left: 26px; top: 24px; }
  .enroll-label { position: absolute; left: 704px; top: 13px; font-size: 22px; letter-spacing: 0.5px; }
  .phone-icon { position: absolute; left: 654px; top: 38px; }
  .phone-number { position: absolute; left: 707px; top: 40px; font-size: 32px; letter-spacing: 1px; }
</style>
</head>
<body>
<main class="flyer">
  <svg class="backdrop" width="927" height="1200" viewBox="0 0 927 1200" aria-hidden="true">
    <rect width="927" height="1200" fill="var(--yellow)"/>
    <path d="M0 0 H927 V40 C650 20 280 50 0 160 Z" fill="var(--red)"/>
    <path d="M0 545 C120 330 420 190 927 190 V1200 H0 Z" fill="var(--white)"/>
    <path d="M560 188 C720 168 860 180 927 188 V245 C820 200 690 188 560 188 Z" fill="var(--green)"/>
    <path d="M0 1010 C300 1020 620 1000 927 950 V1200 H0 Z" fill="var(--yellow)"/>
    <path d="M0 1016 C300 1030 620 1010 927 962 V1200 H0 Z" fill="var(--blue-bright)"/>
  </svg>

  <div class="brand-dot" aria-hidden="true"></div>
  <h1 class="brand">PebbleNest<br>Preschool</h1>

  <svg class="banner" width="927" height="280" viewBox="0 300 927 280" aria-label="Saturday Immersion Language Mandarin and Spanish Lessons for Children Ages 2-5">
    <defs>
      <linearGradient id="ribbon" x1="0" x2="1">
        <stop offset="0" stop-color="var(--green-deep)"/>
        <stop offset="1" stop-color="var(--green)"/>
      </linearGradient>
      <path id="arc1" d="M175 450 C340 373 590 373 755 450"/>
      <path id="arc2" d="M195 485 C350 404 580 404 735 485"/>
      <path id="arc3" d="M270 495 C390 443 540 443 660 495"/>
    </defs>
    <path d="M103 485 L200 485 L200 560 L103 560 L140 522 Z" fill="var(--green-deep)"/>
    <path d="M824 485 L707 485 L707 560 L824 560 L790 522 Z" fill="var(--green-deep)"/>
    <path d="M160 432 C330 330 600 330 768 432 L712 552 C560 450 370 450 215 552 Z" fill="url(#ribbon)"/>
    <text class="banner-text"><textPath href="#arc1" startOffset="50%" text-anchor="middle">Saturday Immersion Language</textPath></text>
    <text class="banner-text"><textPath href="#arc2" startOffset="50%" text-anchor="middle">Mandarin and Spanish Lessons</textPath></text>
    <text class="banner-text"><textPath href="#arc3" startOffset="50%" text-anchor="middle">for Children Ages 2-5</textPath></text>
  </svg>

  <div class="kids-photo" role="img" aria-label="Photo of seven smiling preschool children of different backgrounds standing in a row holding hands"></div>

  <svg class="bubbles" width="927" height="120" viewBox="0 560 927 120" aria-label="Greetings in Spanish and Mandarin">
    <g fill="var(--white)" stroke-width="2.5">
      <path stroke="var(--red)" d="M160 580 a55 40 0 1 1 -25 75 l-15 10 l5 -18 a55 40 0 0 1 35 -67 Z"/>
      <path stroke="var(--green-deep)" d="M358 598 a48 36 0 1 1 -22 66 l-14 8 l5 -16 a48 36 0 0 1 31 -58 Z"/>
      <path stroke="var(--blue)" d="M580 560 a80 55 0 1 1 20 108 l8 14 l-25 -13 a80 55 0 0 1 -3 -109 Z"/>
      <path stroke="var(--orange)" d="M748 588 a50 38 0 1 1 12 74 l5 10 l-18 -10 a50 38 0 0 1 1 -74 Z"/>
    </g>
    <text class="bubble-text" fill="var(--red)" x="160" y="616">Cómo</text>
    <text class="bubble-text" fill="var(--red)" x="160" y="642">estás?</text>
    <text class="bubble-pinyin" fill="var(--green-deep)" x="358" y="617">hā&#8195;&#8195;lou</text>
    <text class="bubble-han" fill="var(--green-deep)" x="358" y="645">哈喽</text>
    <text class="bubble-text" fill="var(--blue)" x="580" y="612">me encanta</text>
    <text class="bubble-text" fill="var(--blue)" x="580" y="640">escuela</text>
    <text class="bubble-pinyin" fill="var(--orange)" x="748" y="612">nǐ&#8195;&#8195;hǎo</text>
    <text class="bubble-han" fill="var(--orange)" x="748" y="640">你好</text>
  </svg>

  <footer class="footer">
    <svg class="route-icon" width="104" height="50" viewBox="0 0 104 50" aria-hidden="true">
      <path d="M4 40 L20 28 L35 38 L52 26 L70 40 L85 30 L100 36" fill="none" stroke="var(--white)" stroke-width="1.5" stroke-dasharray="2 3"/>
      <g fill="var(--yellow)">
        <path d="M10 16 a6 6 0 1 1 12 0 c0 5 -6 11 -6 11 c0 0 -6 -6 -6 -11 Z"/>
        <path d="M50 8 a8 8 0 1 1 16 0 c0 7 -8 14 -8 14 c0 0 -8 -7 -8 -14 Z"/>
        <path d="M88 18 a5 5 0 1 1 10 0 c0 4 -5 9 -5 9 c0 0 -5 -5 -5 -9 Z"/>
        <path d="M76 42 a5 5 0 1 1 10 0 c0 4 -5 8 -5 8 c0 0 -5 -4 -5 -8 Z"/>
      </g>
      <g fill="var(--blue-bright)"><circle cx="16" cy="16" r="2.4"/><circle cx="58" cy="8" r="3"/><circle cx="93" cy="18" r="2"/><circle cx="81" cy="42" r="2"/></g>
    </svg>
    <p class="locations">Locations throughout Washington, DC.</p>
    <p class="enroll-label">Call Now to Enroll</p>
    <svg class="phone-icon" width="44" height="44" viewBox="0 0 44 44" aria-hidden="true">
      <circle cx="22" cy="22" r="19" fill="none" stroke="var(--yellow)" stroke-width="3"/>
      <path d="M15 12 l5 -1 l3 7 l-3 3 c1 3 4 6 7 7 l3 -3 l7 3 l-1 5 c-12 1 -22 -9 -21 -21 Z" fill="var(--yellow)"/>
    </svg>
    <p class="phone-number">202 555 0147</p>
  </footer>
</main>
</body>
</html>
```